Pelkman Agency (http://pa.quorvexstudio.com/)

We are looking for a similar design to what we have, but more professional looking and cleaned up with links and logo that is not so grainy looking. We are an independent insurance agency marketing to personal and commercial clients. We offer all commercial lines markets and all personal lines. We target excavators, landscapers, restaurants, golf courses, contractors. Please look at http://pa.quorvexstudio.com/ which we had designed but do not like it, it will give you an idea of what we are looking for.

Target Market(s)

Commercial and personal insurance. All business products and all personal (homeowners, auto, antique auto, umbrella)

Industry/Entity Type

It Professional

Logo Text

Knowledge Building Your Assurance

Number of Pages Required

5+ page

Colors
000000
848484
0255a3

```html
<!DOCTYPE html>
<html lang="en">
<head>
<meta charset="utf-8">
<title>Pelkman Agency – Website Design</title>
<link rel="stylesheet" href="https://fonts.googleapis.com/css2?family=Questrial&family=Didact+Gothic&display=swap">
<style>
:root{
  --navy:#2f3741;
  --navy-deep:#1c2530;
  --blue:#3a8fc9;
  --blue-soft:#5aa2d6;
  --ink:#222;
  --grey:#555;
  --grey-light:#efefef;
  --card-top:#dcdcdc;
  --white:#fff;
}
*{box-sizing:border-box;margin:0;padding:0}
html,body{width:1200px;height:900px;overflow:hidden;background:#fff}
body{position:relative;font-family:"Didact Gothic","Questrial",sans-serif;color:var(--ink)}
.page{position:absolute;overflow:hidden;background:#fff}
.page-home{left:9px;top:8px;width:478px;height:884px}
.page-personal{left:509px;top:8px;width:681px;height:882px}
.abs{position:absolute}
.brand{position:absolute;display:flex;align-items:center;gap:8px;color:var(--white);font-family:"Questrial",sans-serif;white-space:nowrap}
.brand-dot{border-radius:50%;background:var(--blue)}
.nav{position:absolute;display:flex;font-family:"Questrial",sans-serif;color:var(--white);text-transform:uppercase}
.nav span{display:block}
.nav .active{background:var(--blue)}
.photo{position:absolute}
.blue{color:var(--blue)}
.center{text-align:center}
p{line-height:1.25}
/* home */
.site-header{position:absolute;left:0;top:0;width:100%;background:var(--navy)}
.hero{position:absolute;left:0;top:82px;width:478px;height:197px;background:radial-gradient(ellipse at 50% 70%,#4a5566 0%,#222a35 55%,#141a22 100%)}
.hero-title{position:absolute;top:43px;width:100%;text-align:center;font-family:"Questrial",sans-serif;font-size:33px;color:var(--blue-soft);letter-spacing:1px}
.hero-sub{position:absolute;top:78px;width:100%;text-align:center;font-family:"Questrial",sans-serif;font-size:11px;color:#fff;letter-spacing:4px}
.dots{position:absolute;top:172px;left:213px;display:flex;gap:7px}
.dots i{width:8px;height:8px;border-radius:50%;background:#8a919b;display:block}
.dots i.on{background:var(--blue)}
.rule{position:absolute;height:2px;background:var(--blue)}
.welcome-line{position:absolute;left:0;width:478px;text-align:center;white-space:nowrap;line-height:1}
.welcome-title{top:289px;font-family:"Questrial",sans-serif;font-size:25px;color:var(--blue)}
.welcome-sub{font-family:"Questrial",sans-serif;font-size:12px;color:#111}
.welcome-desc{font-size:7px;color:var(--grey)}
.card{position:absolute;top:424px;width:105px;height:146px;background:#fff}
.card-top{height:41px;background:var(--card-top);display:flex;justify-content:center;align-items:center}
.card h4{font-weight:normal;font-size:8px;text-align:center;margin-top:11px;font-family:"Questrial",sans-serif;white-space:nowrap}
.card p{font-size:5.5px;text-align:center;color:var(--grey);margin:8px 16px 0}
.card .go{position:absolute;right:8px;bottom:8px}
.program{position:absolute;top:712px;width:125px}
.program b{position:absolute;left:0;top:-2px;font-size:20px;font-weight:normal;color:var(--blue)}
.program h5{margin-left:16px;font-size:7px;font-weight:normal;color:var(--blue)}
.program p{margin-left:14px;font-size:5.5px;color:#444;margin-top:3px}
.footer{position:absolute;left:0;width:100%;background:var(--navy);color:#fff}
.footer h6{font-weight:normal;font-family:"Questrial",sans-serif}
.footer ul{list-style:none}
.social{display:flex;align-items:center;gap:6px}
.social i{display:block;background:var(--blue)}
/* personal */
.ins-col{position:absolute;top:213px;width:196px}
.ins-col .photo{position:static;height:100px;width:196px}
.ins-col h3{font-weight:normal;font-family:"Questrial",sans-serif;font-size:13px;color:var(--blue);margin-top:9px;padding-bottom:2px;border-bottom:1px solid var(--blue);width:168px}
.ins-col p{font-size:8.5px;color:#444;margin-top:7px;line-height:1.2}
.offer{position:absolute;left:0;top:450px;width:681px;height:292px;background:linear-gradient(100deg,#f3f5f8 0%,#e6ecf3 45%,#d3dde8 70%,#eef2f6 100%)}
.offer p{font-size:8.5px;color:#444;line-height:1.2}
</style>
</head>
<body>

<section class="page page-home">
  <header class="site-header" style="height:82px">
    <div class="brand" style="left:143px;top:25px;font-size:17px">
      <span class="brand-dot" style="width:25px;height:25px"></span>Pelkman Agency
    </div>
    <nav class="nav" style="left:76px;top:67px;font-size:6px;height:15px;align-items:center">
      <span class="active" style="padding:4px 5px">Home</span>
      <span style="margin-left:13px">Personal</span>
      <span style="margin-left:22px">Business</span>
      <span style="margin-left:24px">Service Center</span>
      <span style="margin-left:21px">About Us</span>
      <span style="margin-left:22px">Contact Us</span>
    </nav>
  </header>
  <div class="hero" role="img" aria-label="Photo of open hands holding small figures of people on a dark background">
    <div class="hero-title">BIG ENOUGH</div>
    <div class="hero-sub">TO MAKE A DIFFERENCE</div>
    <div class="dots"><i></i><i class="on"></i><i></i><i></i></div>
  </div>
  <div class="rule" style="left:0;top:279px;width:478px"></div>

  <h1 class="welcome-line welcome-title" style="font-weight:normal">WELLCOME</h1>
  <div class="welcome-line welcome-sub" style="top:323px">SMALL ENOUGH TO CARE, BIG ENOUGH</div>
  <div class="welcome-line welcome-sub" style="top:337px">TO MAKE A DIFFERENCE</div>
  <div class="welcome-line welcome-desc" style="top:357px">Please find information about our agency,</div>
  <div class="welcome-line welcome-desc" style="top:367px">its principles, and the various types of insurance coverages that we provide.</div>

  <section class="abs" style="left:0;top:389px;width:478px;height:201px;background:var(--grey-light)">
    <h2 class="center" style="font-weight:normal;font-size:11.5px;margin-top:9px;font-family:'Questrial',sans-serif">OUR SERVICES</h2>
  </section>
  <div class="card" style="left:16px"><div class="card-top"><svg width="24" height="24" viewBox="0 0 24 24"><path d="M2 14c3 0 6 3 10 3s7-3 10-3v6H2z" fill="#4a8fc6"/><circle cx="12" cy="8" r="4" fill="#4a8fc6"/></svg></div><h4>BUSINESS INSURANCE</h4><p>Please find information about our agency, its principles, and the various types of insurance coverages that we provide.</p><svg class="go" width="13" height="13" viewBox="0 0 13 13"><circle cx="6.5" cy="6.5" r="5.5" fill="none" stroke="#3a8fc9" stroke-width="1.3"/><path d="M5.5 4l2.5 2.5L5.5 9" fill="none" stroke="#3a8fc9" stroke-width="1.3"/></svg></div>
  <div class="card" style="left:130px"><div class="card-top"><svg width="24" height="24" viewBox="0 0 24 24"><path d="M3 12l3-6h12l3 6v6H3z" fill="#4a8fc6"/><circle cx="7" cy="15" r="1.5" fill="#dcdcdc"/><circle cx="17" cy="15" r="1.5" fill="#dcdcdc"/></svg></div><h4>AUTO INSURANCE</h4><p>Please find information about our agency, its principles, and the various types of insurance coverages that we provide.</p><svg class="go" width="13" height="13" viewBox="0 0 13 13"><circle cx="6.5" cy="6.5" r="5.5" fill="none" stroke="#3a8fc9" stroke-width="1.3"/><path d="M5.5 4l2.5 2.5L5.5 9" fill="none" stroke="#3a8fc9" stroke-width="1.3"/></svg></div>
  <div class="card" style="left:243px"><div class="card-top"><svg width="24" height="24" viewBox="0 0 24 24"><path d="M12 13C6 8 8 3 12 6c4-3 6 2 0 7z" fill="#4a8fc6"/><path d="M2 15c3 0 6 4 10 4s7-4 10-4v5H2z" fill="#4a8fc6"/></svg></div><h4>LIFE INSURANCE</h4><p>Please find information about our agency, its principles, and the various types of insurance coverages that we provide.</p><svg class="go" width="13" height="13" viewBox="0 0 13 13"><circle cx="6.5" cy="6.5" r="5.5" fill="none" stroke="#3a8fc9" stroke-width="1.3"/><path d="M5.5 4l2.5 2.5L5.5 9" fill="none" stroke="#3a8fc9" stroke-width="1.3"/></svg></div>
  <div class="card" style="left:357px"><div class="card-top"><svg width="24" height="24" viewBox="0 0 24 24"><path d="M3 11L12 3l9 8h-3v9H6v-9z" fill="#4a8fc6"/><rect x="10" y="14" width="4" height="6" fill="#dcdcdc"/></svg></div><h4>HOME INSURANCE</h4><p>Please find information about our agency, its principles, and the various types of insurance coverages that we provide.</p><svg class="go" width="13" height="13" viewBox="0 0 13 13"><circle cx="6.5" cy="6.5" r="5.5" fill="none" stroke="#3a8fc9" stroke-width="1.3"/><path d="M5.5 4l2.5 2.5L5.5 9" fill="none" stroke="#3a8fc9" stroke-width="1.3"/></svg></div>

  <section class="abs" style="left:0;top:590px;width:478px;height:82px;background:linear-gradient(90deg,#868a90,#767b82 60%,#9aa0a6)" role="img" aria-label="Muted business photo behind a client testimonial">
    <svg class="abs" style="left:86px;top:24px" width="40" height="34" viewBox="0 0 40 34"><circle cx="17" cy="17" r="16" fill="#3a8fc9"/><circle cx="17" cy="13" r="5" fill="#fff"/><path d="M8 26c2-6 16-6 18 0z" fill="#fff"/><circle cx="31" cy="21" r="8" fill="#2f3741"/><text x="27" y="26" font-size="12" fill="#fff" font-family="serif">”</text></svg>
    <p class="abs" style="left:150px;top:31px;font-size:7px;color:#fff;font-style:italic;white-space:nowrap">“ Please find information about our agency, its principles, ”</p>
    <p class="abs" style="left:156px;top:44px;font-size:7px;color:#a9d2f0;font-style:italic;white-space:nowrap">-Mr. Halden</p>
    <svg class="abs" style="left:380px;top:33px" width="15" height="15" viewBox="0 0 13 13"><circle cx="6.5" cy="6.5" r="5.5" fill="none" stroke="#fff" stroke-width="1.3"/><path d="M5.5 4l2.5 2.5L5.5 9" fill="none" stroke="#fff" stroke-width="1.3"/></svg>
  </section>

  <section class="abs" style="left:0;top:672px;width:478px;height:113px;background:linear-gradient(90deg,#d8dbdf,#eceef0 40%,#c9cdd2 75%,#dfe2e5)" role="img" aria-label="Light photo of a business handshake">
    <h2 class="abs" style="left:29px;top:14px;font-size:11px;font-weight:normal;font-family:'Questrial',sans-serif">WHAT IS NEW</h2>
  </section>
  <div class="program" style="left:26px"><b>1</b><h5>PROGRAM 1</h5><p>Please find information about our agency, its principles, and the various types of insurance coverages that we provide.</p></div>
  <div class="program" style="left:170px"><b>2</b><h5>PROGRAM 2</h5><p>Please find information about our agency, its principles, and the various types of insurance coverages that we provide.</p></div>
  <div class="program" style="left:316px"><b>3</b><h5>PROGRAM 3</h5><p>Please find information about our agency, its principles, and the various types of insurance coverages that we provide.</p></div>

  <footer class="footer" style="top:785px;height:99px">
    <div class="abs" style="left:43px;top:10px;width:95px"><h6 style="font-size:8px;border-bottom:1px solid var(--blue);padding-bottom:3px">NAVIGATION</h6>
      <ul style="font-size:5.8px;line-height:9.3px;margin-top:7px"><li>HOME</li><li>PERSONAL</li><li>BUSINESS</li><li>SERVICE CENTER</li><li>ABOUT US</li><li>CONTACT US</li></ul></div>
    <div class="abs" style="left:193px;top:10px;width:95px"><h6 style="font-size:8px;border-bottom:1px solid var(--blue);padding-bottom:3px">FOLLOW US</h6>
      <div style="font-size:5.8px;margin-top:7px;line-height:11px">
        <div class="social"><i style="width:6px;height:6px"></i>FRIENDPOST</div>
        <div class="social"><i style="width:6px;height:6px"></i>CHIRPLINE</div>
        <div class="social"><i style="width:6px;height:6px"></i>RSS</div></div></div>
    <div class="abs" style="left:342px;top:10px;width:105px"><h6 style="font-size:8px;border-bottom:1px solid var(--blue);padding-bottom:3px">OUR LOCATION</h6>
      <div style="font-size:5.8px;margin-top:7px;line-height:9px;padding-left:15px;position:relative">
        <svg class="abs" style="left:0;top:0" width="6" height="8" viewBox="0 0 6 8"><path d="M3 8L0.5 4A2.6 2.6 0 1 1 5.5 4z" fill="#3a8fc9"/></svg>
        Pelkman Agency<br>418 Orchard Lane, Suite B<br>Millbrook, NJ 07999
        <div style="margin-top:6px;position:relative"><svg class="abs" style="left:-15px;top:1px" width="7" height="7" viewBox="0 0 7 7"><path d="M1 0h2l.5 2L2.5 3a4 4 0 0 0 1.5 1.5L5 3.5l2 .5v2L6 7A6 6 0 0 1 0 1z" fill="#3a8fc9"/></svg>Phone: 555-014-2200<br>Fax: 555-014-7150</div></div></div>
    <div class="rule" style="left:0;bottom:0;width:478px"></div>
  </footer>
</section>

<section class="page page-personal">
  <header class="site-header" style="height:118px;background:var(--navy-deep)">
    <div class="brand" style="left:208px;top:36px;font-size:24px;gap:12px">
      <span class="brand-dot" style="width:34px;height:34px"></span>Pelkman Agency
    </div>
    <nav class="nav" style="left:114px;top:99px;font-size:8px;height:23px;align-items:center">
      <span>Home</span>
      <span class="active" style="margin-left:18px;padding:7px 6px">Personal</span>
      <span style="margin-left:27px">Business</span>
      <span style="margin-left:30px">Service Center</span>
      <span style="margin-left:33px">About Us</span>
      <span style="margin-left:33px">Contact Us</span>
    </nav>
  </header>

  <h1 class="abs blue" style="left:34px;top:154px;font-weight:normal;font-family:'Questrial',sans-serif;font-size:19px;width:306px;border-bottom:1px solid var(--blue);padding-bottom:1px">PERSONAL INSURANCE</h1>
  <h2 class="abs" style="left:34px;top:182px;font-size:10.5px">INSURANCE FOR:</h2>

  <article class="ins-col" style="left:34px">
    <div class="photo" role="img" aria-label="Photo of a smiling retired couple at a cafe" style="background:linear-gradient(120deg,#c9b8a2,#e8ddd0 45%,#b9a18a)"></div>
    <h3>ANNUITY INSURANCE</h3>
    <p>We do not work for an insurance company we work for you. we work on your side when you have a loss and follow through to see that you get affair, prompt, payment. We represent a carefully selected group of reputable insurance companies.</p>
    <p style="margin-top:9px">Please explore our website and let us know how we can help serve your insurance needs.</p>
  </article>
  <article class="ins-col" style="left:242px">
    <div class="photo" role="img" aria-label="Photo of a smiling man seated in a car" style="background:linear-gradient(120deg,#4b5663,#9aa4ae 45%,#2d3540)"></div>
    <h3>CAR INSURANCE</h3>
    <p>We do not work for an insurance company we work for you. we work on your side when you have a loss and follow through to see that you get affair, prompt, payment. We represent a carefully selected group of reputable insurance companies.</p>
    <p style="margin-top:9px">Please explore our website and let us know how we can help serve your insurance needs.</p>
  </article>
  <article class="ins-col" style="left:451px">
    <div class="photo" role="img" aria-label="Photo of a family house with a green lawn under a blue sky" style="background:linear-gradient(180deg,#6aa6dc 0%,#a9cbea 35%,#8a6e5a 55%,#4f8a3a 80%,#3e7a2c)"></div>
    <h3>HOME INSURANCE</h3>
    <p>We do not work for an insurance company we work for you. we work on your side when you have a loss and follow through to see that you get affair, prompt, payment. We represent a carefully selected group of reputable insurance companies.</p>
    <p style="margin-top:9px">Please explore our website and let us know how we can help serve your insurance needs.</p>
  </article>

  <section class="offer" role="img" aria-label="Soft photo of a hand holding a city skyline">
    <h2 class="abs blue" style="left:35px;top:20px;font-weight:normal;font-family:'Questrial',sans-serif;font-size:34px">WE OFFER</h2>
    <p class="abs" style="left:35px;top:58px;font-size:18px;color:#111;line-height:1">Wellcome to our business site</p>
    <div class="photo" role="img" aria-label="Portrait photo of a smiling businesswoman" style="left:38px;top:95px;width:128px;height:102px;background:linear-gradient(120deg,#e9e4df,#c8a690 50%,#5a4a44)"></div>
    <h3 class="abs blue" style="left:177px;top:92px;font-weight:normal;font-size:11px;font-family:'Questrial',sans-serif">WE ENSURE</h3>
    <p class="abs" style="left:177px;top:107px;width:258px">We do not work for an insurance company we work for you. we work on your side when you have a loss and follow through to see that you get affair, prompt, payment. We represent a carefully selected group of reputable insurance companies.</p>
    <p class="abs" style="left:177px;top:158px;width:258px">Please explore our website and let us know how we can help serve your insurance needs.</p>
    <h3 class="abs blue" style="left:453px;top:58px;font-weight:normal;font-size:18px;font-family:'Questrial',sans-serif">HELLOW THERE !</h3>
    <p class="abs" style="left:451px;top:93px;width:194px">We do not work for an insurance company we work for you. we work on your side when you have a loss and follow through to see that you get affair, prompt, payment. We represent a carefully selected group of reputable insurance companies.</p>
    <p class="abs" style="left:451px;top:162px;width:194px">Please explore our website and let us know how we can help serve your insurance needs.</p>
  </section>

  <footer class="footer" style="top:742px;height:140px;background:var(--navy-deep)">
    <div class="abs" style="left:62px;top:14px;width:136px"><h6 style="font-size:12px;border-bottom:1px solid var(--blue);padding-bottom:3px">NAVIGATION</h6>
      <ul style="font-size:8.5px;line-height:13px;margin-top:10px"><li>HOME</li><li>PERSONAL</li><li>BUSINESS</li><li>SERVICE CENTER</li><li>ABOUT US</li><li>CONTACT US</li></ul></div>
    <div class="abs" style="left:276px;top:14px;width:136px"><h6 style="font-size:12px;border-bottom:1px solid var(--blue);padding-bottom:3px">FOLLOW US</h6>
      <div style="font-size:8.5px;margin-top:10px;line-height:17px">
        <div class="social"><i style="width:9px;height:9px"></i>&nbsp;FRIENDPOST</div>
        <div class="social"><i style="width:9px;height:9px"></i>&nbsp;CHIRPLINE</div>
        <div class="social"><i style="width:9px;height:9px"></i>&nbsp;RSS</div></div></div>
    <div class="abs" style="left:487px;top:14px;width:150px"><h6 style="font-size:12px;border-bottom:1px solid var(--blue);padding-bottom:3px;width:136px">OUR LOCATION</h6>
      <div style="font-size:8.5px;margin-top:10px;line-height:13px;padding-left:22px;position:relative">
        <svg class="abs" style="left:0;top:1px" width="8" height="11" viewBox="0 0 6 8"><path d="M3 8L0.5 4A2.6 2.6 0 1 1 5.5 4z" fill="#3a8fc9"/></svg>
        Pelkman Agency<br>418 Orchard Lane, Suite B<br>Millbrook, NJ 07999
        <div style="margin-top:8px;position:relative"><svg class="abs" style="left:-22px;top:1px" width="10" height="10" viewBox="0 0 7 7"><path d="M1 0h2l.5 2L2.5 3a4 4 0 0 0 1.5 1.5L5 3.5l2 .5v2L6 7A6 6 0 0 1 0 1z" fill="#3a8fc9"/></svg>Phone: 555-014-2200<br>Fax: 555-014-7150</div></div></div>
    <div class="rule" style="left:0;bottom:0;width:681px;height:3px"></div>
  </footer>
</section>

</body>
</html>
```